Brightvale Wound Care
Business cards and letterhead
Professional
Gregory Tamsett
Chief Executive Officer
3470 P Street NW
Suite 615
Washington, DC 20011
gtamsett@brightvale-wc.example
www.brightvale-wc.example
I need one that says "CEO" for the name above and one that says "Territory Manager". I also need (with the same design for the name Darren Pulcombe as "President" and one for him as well that says Senior Territory Manager"
I need to list these products on the back:
1. Verashu Negitive Pressure Wound Therapy
2. Brunix Negitive Pressure Wound Therapy
3. Orvil alternating pressure mattresses
Here is our logo please use this logo while doing our design for this project for both the business cards and letterhead. Thanks
Please add this one or the non-green one (also uploaded) some where on the card. Make it very small please.
Or add this one to the card somewhere. Whatever one looks better.

```html
<!DOCTYPE html>
<html lang="en">
<head>
<meta charset="utf-8">
<title>Brightvale Wound Care – Stationery</title>
<link href="https://fonts.googleapis.com/css2?family=Arimo:wght@400;700&display=swap" rel="stylesheet">
<style>
  :root{
    --stage:#000;
    --paper:#fff;
    --navy:#27288a;
    --red:#d3122b;
    --ink:#1c1c5a;
    --muted:#e9e9ee;
  }
  *{box-sizing:border-box;margin:0;padding:0}
  html,body{width:1200px;height:801px;overflow:hidden;background:var(--stage);font-family:"Arimo",Arial,sans-serif}
  .stage{position:relative;width:1200px;height:801px}

  .brand{display:flex;align-items:center;gap:6px;color:var(--navy);font-weight:700;white-space:nowrap}
  .brand-dot{border-radius:50%;background:var(--red);flex:none}

  .seal{position:absolute;background:var(--muted);border:1px solid #b8b8c8}

  /* Letterhead */
  .letterhead{position:absolute;left:19px;top:48px;width:552px;height:715px;background:var(--paper);overflow:hidden}
  .letterhead .brand{position:absolute;right:38px;top:44px;font-size:16px;gap:5px}
  .letterhead .brand-dot{width:18px;height:18px}
  .letterhead .seal{left:492px;top:620px;width:26px;height:26px}
  .letterhead-rule{position:absolute;left:0;right:0;top:662px;height:2px;background:var(--red)}
  .letterhead-footer{position:absolute;left:0;right:0;top:672px;text-align:center;color:var(--navy);font-size:9px;font-weight:700;line-height:13px}

  /* Business cards */
  .card{position:absolute;width:226px;height:137px;background:var(--paper);overflow:hidden}
  .card-band{position:absolute;inset:0}
  .card .brand{position:absolute;left:10px;top:14px;font-size:11.5px;gap:4px}
  .card .brand-dot{width:11px;height:11px}
  .card-person{position:absolute;right:10px;top:60px;text-align:right}
  .card-name{color:#fff;font-weight:700;font-size:9px}
  .card-title{color:#fff;font-size:6.5px;margin-top:1px}
  .card-contact{position:absolute;left:10px;top:62px;color:#fff;font-size:6px;line-height:8px}
  .card .seal{right:10px;top:10px;width:14px;height:14px}

  .card-back{position:absolute;left:710px;top:335px;width:228px;height:120px;overflow:hidden}
  .card-back ol{position:absolute;left:16px;top:34px;color:#fff;font-size:7px;line-height:11px;font-weight:700;list-style-position:inside;text-transform:uppercase}

  /* Envelope */
  .envelope{position:absolute;left:595px;top:465px;width:586px;height:259px;background:var(--paper);overflow:hidden}
  .envelope .brand{position:absolute;left:14px;top:38px;font-size:17px;gap:5px}
  .envelope .brand-dot{width:19px;height:19px}
  .envelope-return{position:absolute;left:22px;top:180px;color:var(--navy);font-size:7px;font-weight:700;line-height:10px}
  .envelope .seal{left:172px;top:210px;width:22px;height:22px}
</style>
</head>
<body>
<main class="stage">

  <svg width="0" height="0" style="position:absolute" aria-hidden="true">
    <defs>
      <linearGradient id="band" x1="0" y1="0" x2="1" y2="0">
        <stop offset="0" stop-color="#27288a"/>
        <stop offset="0.55" stop-color="#3b2a8e"/>
        <stop offset="1" stop-color="#d3122b"/>
      </linearGradient>
    </defs>
  </svg>

  <!-- Letterhead -->
  <section class="letterhead">
    <div class="brand"><span class="brand-dot"></span>Brightvale Wound Care</div>
    <div class="seal" aria-label="Accreditation seal"></div>
    <div class="letterhead-rule"></div>
    <div class="letterhead-footer">
      3470 P Street NW, Suite 615, Washington, DC 20011<br>
      Phone : 202-555-0147 / Fax : 202-555-0183 / Web : www.brightvale-wc.example
    </div>
  </section>

  <!-- Card: Gregory Tamsett, CEO -->
  <article class="card" style="left:595px;top:48px">
    <svg class="card-band" viewBox="0 0 226 137" aria-hidden="true">
      <path d="M0 56 Q120 44 226 58 L226 137 L0 137Z" fill="url(#band)"/>
      <path d="M120 137 Q150 80 226 70" fill="none" stroke="#fff" stroke-opacity=".15" stroke-width="6"/>
    </svg>
    <div class="brand"><span class="brand-dot"></span>Brightvale Wound Care</div>
    <div class="card-person"><div class="card-name">Gregory Tamsett</div><div class="card-title">CEO</div></div>
    <div class="card-contact">3470 P Street NW<br>Suite 615<br>Washington, DC 20011<br>Phone : 202-555-0147<br>Fax : 202-555-0183<br>Email : gtamsett@brightvale-wc.example<br>Web : www.brightvale-wc.example</div>
  </article>

  <!-- Card: Gregory Tamsett, Territory Manager -->
  <article class="card" style="left:845px;top:48px">
    <svg class="card-band" viewBox="0 0 226 137" aria-hidden="true">
      <path d="M0 56 Q120 44 226 58 L226 137 L0 137Z" fill="url(#band)"/>
      <path d="M120 137 Q150 80 226 70" fill="none" stroke="#fff" stroke-opacity=".15" stroke-width="6"/>
    </svg>
    <div class="brand"><span class="brand-dot"></span>Brightvale Wound Care</div>
    <div class="card-person"><div class="card-name">Gregory Tamsett</div><div class="card-title">Territory Manager</div></div>
    <div class="card-contact">3470 P Street NW<br>Suite 615<br>Washington, DC 20011<br>Phone : 202-555-0147<br>Fax : 202-555-0183<br>Email : gtamsett@brightvale-wc.example<br>Web : www.brightvale-wc.example</div>
  </article>

  <!-- Card: Darren Pulcombe, President -->
  <article class="card" style="left:595px;top:194px">
    <svg class="card-band" viewBox="0 0 226 137" aria-hidden="true">
      <path d="M0 56 Q120 44 226 58 L226 137 L0 137Z" fill="url(#band)"/>
      <path d="M120 137 Q150 80 226 70" fill="none" stroke="#fff" stroke-opacity=".15" stroke-width="6"/>
    </svg>
    <div class="brand"><span class="brand-dot"></span>Brightvale Wound Care</div>
    <div class="seal" aria-label="Accreditation seal"></div>
    <div class="card-person"><div class="card-name">Darren Pulcombe</div><div class="card-title">President</div></div>
    <div class="card-contact">3470 P Street NW<br>Suite 615<br>Washington, DC 20011<br>Phone : 202-555-0147<br>Fax : 202-555-0183<br>Web : www.brightvale-wc.example</div>
  </article>

  <!-- Card: Darren Pulcombe, Senior Territory Manager -->
  <article class="card" style="left:845px;top:194px">
    <svg class="card-band" viewBox="0 0 226 137" aria-hidden="true">
      <path d="M0 56 Q120 44 226 58 L226 137 L0 137Z" fill="url(#band)"/>
      <path d="M120 137 Q150 80 226 70" fill="none" stroke="#fff" stroke-opacity=".15" stroke-width="6"/>
    </svg>
    <div class="brand"><span class="brand-dot"></span>Brightvale Wound Care</div>
    <div class="seal" aria-label="Accreditation seal"></div>
    <div class="card-person"><div class="card-name">Darren Pulcombe</div><div class="card-title">Senior Territory Manager</div></div>
    <div class="card-contact">3470 P Street NW<br>Suite 615<br>Washington, DC 20011<br>Phone : 202-555-0147<br>Fax : 202-555-0183<br>Web : www.brightvale-wc.example</div>
  </article>

  <!-- Card back: products -->
  <article class="card-back">
    <svg class="card-band" viewBox="0 0 228 120" width="228" height="120" aria-hidden="true">
      <rect width="228" height="120" fill="url(#band)"/>
      <path d="M110 120 Q150 60 228 50" fill="none" stroke="#fff" stroke-opacity=".15" stroke-width="8"/>
    </svg>
    <ol>
      <li>Verashu Negative Pressure Wound Therapy</li>
      <li>Brunix Negative Pressure Wound Therapy</li>
      <li>Orvil Alternating Pressure Mattresses</li>
    </ol>
  </article>

  <!-- Envelope -->
  <section class="envelope">
    <div class="brand"><span class="brand-dot"></span>Brightvale Wound Care</div>
    <div class="envelope-return">3470 P Street NW<br>Suite 615<br>Washington, DC 20011<br>Phone : 202-555-0147<br>Fax : 202-555-0183<br>Web : www.brightvale-wc.example</div>
    <div class="seal" aria-label="Accreditation seal"></div>
  </section>

</main>
</body>
</html>
```